Luxury Wine Label for New Startup Winery

We need a wine label for our new winery startup. We have worked with a local designer but do not feel the resulting label / logo have the elevation required to present our brand as a luxury wine. Our winery is called "Harrowgate Vineyards" and we are focused on extremely high quality hand crafted artisan and estate wines from the Pacific Northwest.
We would like to see designs that utilize a tree line, or other imagery that represents the "Harrowgate" part of our company name. Another interesting feature could be wood grain.
A logo will be required based on your design so please design with this in mind:
This logo should be consistent with the wine bottle label design, and should be representative of our high end exclusive wine while giving a sense of place (Oregon/ Pacific Northwest.)
I will supply an image of the design we received from our local designer, PLEASE NOTE: in general we do like wood grain and tree line concepts but feel the execution was poorly done.
ATTN: Logo design should be suitable for use on: Bottles (Red wine/rose/white wine), Bussiness cards, vehicle signage, business signage, etc
P.S.:
If you have a design that is not outside the box we are still interested in seeing it.
Label is for a burgundy style bottle with a label height of 3.5 - 4" and a width of 3.5-4"
any label <= 4"x4" and >=3.5"x3.5" will be acceptable:
HOWEVER Width should be greater than or equal to height due to the bottle format
Target Market(s)
Wine enthusiasts with adequate discretionary budgets to afford $100 bottles of wine.
Industry/Entity Type
Wine / Winery
Requirements
Must have
- A sense of luxury, a feel of exclusivity, and a theme consistent with our product and brand name
Nice to have
- Tree line, wood grain or other wood themes. Serif fonts
Should not have
- anything cheesy, off topic, hard to read script fonts or anything that makes the label hard to read from a few feet away or too busy

```html
<!DOCTYPE html>
<html lang="en">
<head>
<meta charset="utf-8">
<title>Harrowgate Vineyards — Syrah Label</title>
<link rel="stylesheet" href="https://fonts.googleapis.com/css2?family=Cinzel:wght@400;500&family=Pinyon+Script&display=swap">
<style>
  :root {
    --backdrop-light: #e4e4e4;
    --backdrop-dark: #b9b9b9;
    --label-black: #1f1f21;
    --rule-white: #ececec;
    --text-white: #f2f2f0;
    --text-soft: #d6d6d4;
    --gold: #c39a45;
    --gold-light: #e2c27a;
    --wood-dark: #5a2614;
    --wood-mid: #8a4326;
    --wood-light: #a45a33;
  }
  * { margin: 0; padding: 0; box-sizing: border-box; }
  html, body {
    width: 1200px;
    height: 750px;
    overflow: hidden;
  }
  body {
    background: radial-gradient(ellipse at 50% 40%, var(--backdrop-light) 0%, var(--backdrop-dark) 100%);
    position: relative;
  }
  .wine-label {
    position: absolute;
    left: 342px;
    top: 101px;
    width: 516px;
  }
  .label-main {
    position: relative;
    height: 419px;
    background: var(--label-black);
    box-shadow: 0 2px 8px rgba(0,0,0,0.18);
  }
  .label-rule {
    position: absolute;
    left: 64px;
    right: 64px;
    height: 2px;
    background: var(--rule-white);
  }
  .label-rule--top { top: 50px; }
  .label-rule--bottom { top: 368px; }
  .brand-name {
    position: absolute;
    left: 0;
    right: 0;
    top: 208px;
    text-align: center;
    font-family: "Cinzel", serif;
    font-weight: 400;
    color: var(--text-white);
    line-height: 1;
  }
  .brand-name__primary {
    display: block;
    font-size: 36px;
    letter-spacing: 3px;
  }
  .brand-name__secondary {
    display: block;
    margin-top: 12px;
    font-size: 17px;
    letter-spacing: 4px;
  }
  .appellation {
    position: absolute;
    left: 0;
    right: 0;
    top: 307px;
    text-align: center;
    font-family: "Cinzel", serif;
    font-size: 18px;
    letter-spacing: 1px;
    color: var(--text-soft);
  }
  .label-varietal {
    position: relative;
    margin-top: 5px;
    height: 125px;
    box-shadow: 0 2px 8px rgba(0,0,0,0.18);
    overflow: hidden;
  }
  .wood-grain {
    position: absolute;
    inset: 0;
    background: linear-gradient(100deg, var(--wood-dark) 0%, var(--wood-mid) 30%, var(--wood-light) 55%, var(--wood-mid) 78%, var(--wood-dark) 100%);
  }
  .gold-edge {
    position: absolute;
    left: 0;
    right: 0;
    height: 4px;
    background: linear-gradient(90deg, var(--gold), var(--gold-light), var(--gold));
  }
  .gold-edge--top { top: 8px; }
  .gold-edge--bottom { bottom: 8px; }
  .varietal-name {
    position: absolute;
    left: 0;
    right: 0;
    top: 20px;
    text-align: center;
    font-family: "Pinyon Script", cursive;
    font-size: 44px;
    color: var(--gold-light);
    line-height: 1;
  }
  .vintage-line {
    position: absolute;
    left: 0;
    right: 0;
    top: 84px;
    text-align: center;
    font-family: "Cinzel", serif;
    font-size: 14px;
    letter-spacing: 2px;
    color: var(--text-white);
  }
</style>
</head>
<body>
  <div class="wine-label">
    <section class="label-main">
      <div class="label-rule label-rule--top"></div>
      <h1 class="brand-name">
        <span class="brand-name__primary">Harrowgate</span>
        <span class="brand-name__secondary">Vineyards</span>
      </h1>
      <p class="appellation">Willamette Valley</p>
      <div class="label-rule label-rule--bottom"></div>
    </section>
    <section class="label-varietal">
      <div class="wood-grain" role="img" aria-label="Polished reddish-brown wood grain texture"></div>
      <div class="gold-edge gold-edge--top"></div>
      <div class="gold-edge gold-edge--bottom"></div>
      <p class="varietal-name">Syrah</p>
      <p class="vintage-line">ESTATE | 2023 | GROWN</p>
    </section>
  </div>
</body>
</html>
```